BRISKA sparkling water needs new artwork! Based in Southern California

"Briska" is a new sparkling water company based in Southern California that offers refreshing flavors (lime, cherry, & mango) with B vitamins and antioxidants.

We would like to see packaging designs for standard 12oz cans for each of the three flavors.
Our initial preference is to have individual artwork for each flavor.

Attached are examples of competitors' designs.
Updates

We are extending the deadline for the Thanksgiving Holiday. Thank you all for your contributions.

```html
<!DOCTYPE html>
<html lang="en">
<head>
<meta charset="utf-8">
<title>Briska Sparkling Water – Can Labels</title>
<link href="https://fonts.googleapis.com/css2?family=Josefin+Sans:wght@400;600;700&family=Questrial&display=swap" rel="stylesheet">
<style>
  :root {
    --bg: #c3d3e5;
    --label: #ffffff;
    --ink: #1b1b1b;
    --cherry: #b3262b;
    --cherry-dark: #4a1616;
    --cherry-band: #4d1a1a;
    --lime: #7cc242;
    --lime-dark: #1f4d1d;
    --lime-band: #2f6a2a;
    --mango: #e3b21c;
    --mango-dark: #3a2a10;
    --mango-band: #4a3b14;
  }
  * { box-sizing: border-box; margin: 0; padding: 0; }
  html, body { width: 1200px; height: 930px; overflow: hidden; }
  body {
    background: var(--bg);
    font-family: "Questrial", sans-serif;
    display: flex;
    justify-content: center;
    align-items: center;
    gap: 50px;
  }
  .can-label {
    width: 320px;
    height: 760px;
    background: var(--label);
    display: flex;
    flex-direction: column;
    align-items: center;
    border-radius: 6px;
    overflow: hidden;
    box-shadow: 0 10px 30px rgba(40, 60, 90, 0.18);
  }
  .claim-band {
    width: 100%;
    height: 44px;
    display: flex;
    justify-content: space-around;
    align-items: center;
    color: #fff;
    font-size: 13px;
    letter-spacing: 0.5px;
  }
  .brand-name {
    margin-top: 30px;
    font-family: "Josefin Sans", sans-serif;
    font-weight: 600;
    font-size: 52px;
    color: var(--ink);
    letter-spacing: 0.5px;
  }
  .flow-art {
    margin-top: 26px;
    width: 100%;
    height: 380px;
    border-radius: 48% 52% 46% 54% / 30% 40% 60% 70%;
  }
  .flavor-name {
    margin-top: 52px;
    font-family: "Josefin Sans", sans-serif;
    font-weight: 700;
    font-size: 36px;
    letter-spacing: 7px;
  }
  .product-type {
    margin-top: 6px;
    font-size: 20px;
    letter-spacing: 1px;
  }
  .volume {
    margin-top: 22px;
    font-size: 12px;
    color: var(--ink);
  }
  .cherry .claim-band { background: var(--cherry-band); }
  .cherry .flow-art { background: linear-gradient(160deg, var(--cherry) 0%, #7d1f20 50%, var(--cherry-dark) 100%); }
  .cherry .flavor-name, .cherry .product-type { color: var(--cherry); }
  .lime .claim-band { background: var(--lime-band); }
  .lime .flow-art { background: linear-gradient(160deg, var(--lime) 0%, #3f8a2f 50%, var(--lime-dark) 100%); }
  .lime .flavor-name, .lime .product-type { color: var(--lime); }
  .mango .claim-band { background: var(--mango-band); }
  .mango .flow-art { background: linear-gradient(160deg, var(--mango) 0%, #a07414 50%, var(--mango-dark) 100%); }
  .mango .flavor-name, .mango .product-type { color: var(--mango); }
</style>
</head>
<body>
  <section class="can-label cherry">
    <div class="claim-band"><span>Antioxidant</span><span>Vitamin B</span><span>Antioxidant</span></div>
    <div class="brand-name">Briska</div>
    <div class="flow-art" role="img" aria-label="Layered flowing ribbon illustration in cherry reds and deep brown"></div>
    <div class="flavor-name">CHERRY</div>
    <div class="product-type">Sparkling Water</div>
    <div class="volume">12 fl oz (250ml)</div>
  </section>
  <section class="can-label lime">
    <div class="claim-band"><span>Antioxidant</span><span>Vitamin B</span><span>Antioxidant</span></div>
    <div class="brand-name">Briska</div>
    <div class="flow-art" role="img" aria-label="Layered flowing ribbon illustration in lime greens and dark green"></div>
    <div class="flavor-name">LIME</div>
    <div class="product-type">Sparkling Water</div>
    <div class="volume">12 fl oz (250ml)</div>
  </section>
  <section class="can-label mango">
    <div class="claim-band"><span>Antioxidant</span><span>Vitamin B</span><span>Antioxidant</span></div>
    <div class="brand-name">Briska</div>
    <div class="flow-art" role="img" aria-label="Layered flowing ribbon illustration in mango yellows and dark brown"></div>
    <div class="flavor-name">MANGO</div>
    <div class="product-type">Sparkling Water</div>
    <div class="volume">12 fl oz (250ml)</div>
  </section>
</body>
</html>
```